Visitenkarten für Mentorin für Frauen
Zielgruppe
Ich bin Mentorin für Frauen (30-50 Jahre alt), die ihre Berufung endlich finden möchten und sich nach mehr Energie und Sinn sehnen. Ich helfe ihnen mit meiner (Name fehtl noch)-Methode ihren Seelenweg zu finden und zu gehen, sodass sie vor Energie übersprudeln und mit einem Leuchten in den Augen ein Leben in Fluss und Fülle kreieren.
Sie sind nicht unglücklich, aber es fehtl ihnen was, das sie wirklich erfüllt.
Stichwörter: Numerologie, Human Design, Seelenweg, Berufung, Lebensaufgabe, erfüllt sein- endlich die Leere füllen, Freiheit, Selbstbestimmt, Selbstliebe, Potentialentfaltung, Transformation
meine core story:
Mit Freude, unglaublicher Energie und einem Strahlen in den Augen schon vor dem Wecker aufzustehen, war für mich früher undenkbar. Ich konnte mir nicht vorstellen, wie sich Leute auf den Montag freuen konnten.
Dabei hätte mich nicht als unglücklich bezeichnet, aber es fehlt einfach etwas, ich hatte eine innere Leere und eine Sehnsucht nach dem Sinn in meinem Lebe, wollte so geliebt werden wie ich bin und mich auch so zeigen können. Ich weiß wie es ist sich klein, unsicher zu fühlen und nicht zu wissen woher das kommt. Ich habe es einfach nicht für möglich gehalten, dass diese innere Leere so leicht zu füllen ist und Freude, Spaß, Selbstbewusstseein und Leichtigkeit in allen Bereichen mit sich bringt.
Weil ich selbst diesen Weg gegangen bin und weil ich weiß, dass es nichts erfüllenderes gibt als das schlummernde Potential zu erwecken, begleite ich Frauen dabei ihren Seelenweg zu finden und zu gehen.
Dadurch dass sie genau wissen, was ihre Gaben sind und was ihre Seele glücklich macht, haben sie Spaß und Freude, gerade auch in den alltäglichen Dingen. Sie führen ein selbstbestimmtes Leben, lieben sich selbst und zeigen sich so wie sie sind.Die gigantische Energie die dadurch in ihnen frei wird, lässt sie die bisherigen Grenzen überwinden. Sie tun was sie erfüllt, o..
Aufgabenstellung
weiblich, geschwungen, weich: beinhalten solls:
Hannelore Wiebke
Mentorin für Powerfrauen
(Lebe deine Berufung)--> da bin ich mir nicht ganz sicher ob das gut aussehn wird oder zuviel wird
falls relevant habe ich bisher folgende Schriftarten verwendet: Canva Sans und Tan mon cheri
ist aber kein muss

```html
<!DOCTYPE html>
<html lang="de">
<head>
<meta charset="UTF-8">
<title>Hannelore Wiebke – Visitenkarte</title>
<link rel="stylesheet" href="https://fonts.googleapis.com/css2?family=Great+Vibes&family=Open+Sans:wght@300;400&display=swap">
<style>
  :root {
    --card-bg: #dbc8b9;
    --ink: #7a6152;
    --ink-soft: #83706a;
    --art-tone: #e6d9cd;
    --art-tone-fade: rgba(230, 217, 205, 0);
  }
  html, body {
    margin: 0;
    padding: 0;
    overflow: hidden;
    background: var(--card-bg);
  }
  .card {
    position: relative;
    width: 1200px;
    height: 686px;
    background: var(--card-bg);
    overflow: hidden;
    font-family: "Open Sans", Arial, sans-serif;
    color: var(--ink-soft);
  }
  .name {
    position: absolute;
    left: 64px;
    top: 20px;
    margin: 0;
    font-family: "Great Vibes", cursive;
    font-weight: 400;
    font-size: 118px;
    line-height: 118px;
    color: var(--ink);
  }
  .name .line { display: block; }
  .name .line-second { margin-left: -14px; }
  .art {
    position: absolute;
    border-radius: 48%;
  }
  .art-hand-flowers {
    left: 486px;
    top: 56px;
    width: 260px;
    height: 630px;
    border-radius: 130px 130px 0 0;
    background: radial-gradient(ellipse at 50% 45%, var(--art-tone) 0%, var(--art-tone-fade) 72%);
  }
  .art-portrait {
    left: 130px;
    top: 446px;
    width: 280px;
    height: 240px;
    border-radius: 140px 140px 0 0;
    background: radial-gradient(ellipse at 50% 60%, var(--art-tone) 0%, var(--art-tone-fade) 72%);
  }
  .art-sparkles {
    left: 690px;
    top: 0;
    width: 450px;
    height: 320px;
    background: radial-gradient(ellipse at 78% 40%, var(--art-tone) 0%, var(--art-tone-fade) 60%);
  }
  .tagline {
    position: absolute;
    right: 86px;
    top: 264px;
    margin: 0;
    text-align: right;
    font-weight: 300;
    font-size: 42px;
    line-height: 57px;
    letter-spacing: 4.5px;
    text-transform: uppercase;
  }
  .contact {
    position: absolute;
    right: 86px;
    top: 404px;
    margin: 0;
    padding: 0;
    list-style: none;
    text-align: right;
    font-weight: 400;
    font-size: 32px;
    line-height: 50px;
    letter-spacing: 2px;
  }
</style>
</head>
<body>
  <main class="card">
    <div class="art art-sparkles" role="img" aria-label="Funkelnde Sterne als feine Linienzeichnung"></div>
    <div class="art art-hand-flowers" role="img" aria-label="Linienzeichnung einer Hand, die einen Blumenzweig hält, umgeben von kleinen Sternen"></div>
    <div class="art art-portrait" role="img" aria-label="Linienzeichnung einer Frau im Profil mit Blüte im Haar"></div>

    <h1 class="name">
      <span class="line">Hannelore</span>
      <span class="line line-second">Wiebke</span>
    </h1>

    <p class="tagline">Mentorin für<br>Powerfrauen</p>

    <ul class="contact">
      <li class="contact-web">seelenweg-wiebke.de</li>
      <li class="contact-social">@seelenweg.wiebke</li>
      <li class="contact-phone">+49 151 2468 3570</li>
    </ul>
  </main>
</body>
</html>
```